Business card design

I already have the logo design completed and am requiring business card design and layout utilising the logo. I require a front and back design.

We are an executive recruitment company so we are looking at full colour, high finish in a reasonably conservative structure.
Updates

Reason: will be provide ai template

Target Market(s)

Senior Management 35-60 age bracket

Industry/Entity Type

Business

Requirements
Must have
• Tobias Wrenfield
• Director
• 48 Morrow Pde, Paddington QLD 4064
• Ph: 07 3944 2618 Mob: 0468925317
• tobias@orvandaexecutive.com.au
• www.orvandaexecutive.com.au
Nice to have
• Ideally full colour,
Should not have
• cheap looking

```html
<!DOCTYPE html>
<html lang="en">
<head>
<meta charset="utf-8">
<title>Orvanda Executive – Business Cards</title>
<link rel="stylesheet" href="https://fonts.googleapis.com/css2?family=Montserrat:wght@400;500;600;700&display=swap">
<style>
  :root {
    --navy: #0a3f74;
    --navy-deep: #073461;
    --navy-light: #0c4a86;
    --paper: #f4f4f2;
    --ink-grey: #4a4f57;
    --rule: #9aa3ad;
    --backdrop: #e6e6e4;
    --white: #ffffff;
  }
  * { box-sizing: border-box; margin: 0; padding: 0; }
  html, body {
    width: 1200px;
    height: 1200px;
    overflow: hidden;
  }
  body {
    background: var(--backdrop);
    font-family: "Montserrat", Arial, sans-serif;
    position: relative;
  }
  .card {
    position: absolute;
    left: 170px;
    width: 860px;
    height: 525px;
    border-radius: 4px;
    box-shadow: 0 6px 18px rgba(0,0,0,0.12);
  }

  /* Contact side */
  .card--contact {
    top: 50px;
    background: var(--paper);
  }
  .brand {
    display: flex;
    align-items: center;
    gap: 14px;
  }
  .brand__mark {
    border-radius: 50%;
    flex: none;
  }
  .brand__name {
    font-weight: 700;
    text-transform: uppercase;
    white-space: nowrap;
  }
  .card--contact .brand {
    position: absolute;
    left: 70px;
    top: 175px;
  }
  .card--contact .brand__mark {
    width: 34px;
    height: 34px;
    background: var(--navy);
  }
  .card--contact .brand__name {
    font-size: 21px;
    letter-spacing: 1px;
    color: var(--navy);
  }
  .divider {
    position: absolute;
    left: 430px;
    top: 100px;
    width: 2px;
    height: 250px;
    background: var(--rule);
  }
  .contact {
    position: absolute;
    left: 470px;
    top: 112px;
    color: var(--ink-grey);
  }
  .contact__name {
    font-size: 38px;
    font-weight: 700;
    letter-spacing: 1px;
    color: var(--navy);
    line-height: 1.1;
    margin-bottom: 8px;
  }
  .contact__line {
    font-size: 15px;
    font-weight: 500;
    letter-spacing: 0.8px;
    line-height: 1.55;
  }
  .contact__line--email {
    font-size: 14px;
    letter-spacing: 0.3px;
  }
  .contact__address {
    margin-top: 26px;
  }
  .card--contact .web {
    position: absolute;
    left: 70px;
    top: 410px;
    font-size: 26px;
    font-weight: 600;
    letter-spacing: 2.5px;
    color: var(--navy);
  }

  /* Brand side */
  .card--brand {
    top: 625px;
    background: linear-gradient(160deg, var(--navy-light) 0%, var(--navy) 55%, var(--navy-deep) 100%);
    color: var(--white);
  }
  .card--brand .brand {
    position: absolute;
    left: 0;
    right: 0;
    top: 200px;
    justify-content: center;
    gap: 22px;
  }
  .card--brand .brand__mark {
    width: 62px;
    height: 62px;
    background: var(--white);
  }
  .card--brand .brand__name {
    font-size: 42px;
    letter-spacing: 2px;
    color: var(--white);
  }
  .card--brand .web {
    position: absolute;
    left: 0;
    right: 0;
    top: 400px;
    text-align: center;
    font-size: 28px;
    font-weight: 500;
    letter-spacing: 3px;
    color: var(--white);
  }
</style>
</head>
<body>
  <section class="card card--contact" aria-label="Business card, contact side">
    <div class="brand">
      <span class="brand__mark"></span>
      <span class="brand__name">Orvanda Executive</span>
    </div>
    <div class="divider"></div>
    <div class="contact">
      <p class="contact__name">NAME</p>
      <p class="contact__line">XXXX XXX XXX</p>
      <p class="contact__line contact__line--email">admin@orvandaexecutive.com.au</p>
      <div class="contact__address">
        <p class="contact__line">PO BOX XX</p>
        <p class="contact__line">XXXX XXXX XXXX</p>
        <p class="contact__line">XXXX XX</p>
      </div>
    </div>
    <p class="web">www.orvandaexecutive.com.au</p>
  </section>

  <section class="card card--brand" aria-label="Business card, brand side">
    <div class="brand">
      <span class="brand__mark"></span>
      <span class="brand__name">Orvanda Executive</span>
    </div>
    <p class="web">www.orvandaexecutive.com.au</p>
  </section>
</body>
</html>
```